Dermiva clinic Website for young modern clinic

Website for dermiva clinic
To be modern and sleek.
Clinic base - are young and modern.
Images
Main treatments are Dermiva and lip enhancement
Needs to include
Link to Facebook
Link to twitter
Price list
Room for a small brief on each item
Hours
Mon 10-4pm
Tues 10-4pm
Wed 12-8pm
Thurs Quenby Row 0700-4pm
Friday 10- 2pm
Saturday 9am - 2pm
Booking page/calender
Where we are - map
Address:
52 Wexmoor Lane, 4 Fenbrook Parade TN9 4QW
Phone number 0207 384 9102 or 07914385217
Company Name: NPA
Address: 52 Wexmoor Lane, 4 Fenbrook Parade, TN9 4QW
Phone: 0207 384 9102
Website: www.nessapelbourneaesthetics.co.uk
Clinic
3 page

```html
<!DOCTYPE html>
<html lang="en">
<head>
<meta charset="utf-8">
<title>Nessa Pelbourne Aesthetics</title>
<link href="https://fonts.googleapis.com/css2?family=Lato:wght@300;400;700&family=Open+Sans:wght@400;600&display=swap" rel="stylesheet">
<style>
:root{
  --coral:#f07f63;
  --dark:#4a4a4c;
  --text:#333;
  --muted:#888;
  --light:#f2f2f2;
  --btn-grey:#a9a9ab;
  --amber:#f5a623;
  --red:#d9534f;
  --slate:#5b6a80;
  --teal:#2bb5a0;
  --white:#fff;
}
*{margin:0;padding:0;box-sizing:border-box}
html,body{width:1200px;height:2217px;overflow:hidden}
body{position:relative;background:var(--white);font-family:"Open Sans",Arial,sans-serif;color:var(--text)}
h1,h2{font-weight:400}
.abs{position:absolute}
.topline{left:0;top:0;width:1200px;height:6px;background:#e4e4e4}

/* header */
.brand{left:155px;top:24px;display:flex;align-items:center;gap:14px}
.brand-dot{width:58px;height:58px;border-radius:50%;background:#b9b9bb}
.brand-name{font-family:"Lato",sans-serif;font-weight:400;font-size:17px;line-height:21px;color:#8c8c8e;letter-spacing:1px}
.call{left:732px;top:30px;font-family:"Lato",sans-serif;font-size:20px;color:#8c8c8e;display:flex;align-items:center;gap:8px}
.social-top{left:1000px;top:34px;display:flex;gap:6px}
.soc{width:17px;height:17px;border-radius:50%;background:#b4b4b6}
.soc.on{background:var(--coral)}
.nav{left:423px;top:89px;width:625px;height:24px;font-family:"Lato",sans-serif;font-size:15px;color:var(--text)}
.nav span{position:absolute;top:0;white-space:nowrap}
.nav .active{color:var(--coral)}
.nav-caret{left:433px;top:124px;width:0;height:0;border-left:8px solid transparent;border-right:8px solid transparent;border-bottom:8px solid var(--coral)}

/* hero */
.hero{left:0;top:132px;width:1200px;height:478px;background:linear-gradient(100deg,#3a4650 0%,#56656e 45%,#3d4a52 100%)}
.hero-title{left:155px;top:222px;font-family:"Lato",sans-serif;font-weight:300;font-size:28px;line-height:37px;color:var(--white)}
.hero-copy{left:155px;top:305px;width:410px;font-size:13px;line-height:19px;color:#eee}
.btn{display:flex;align-items:center;justify-content:center;font-family:"Lato",sans-serif;font-size:12px;letter-spacing:1.4px;color:var(--white);text-transform:uppercase;box-shadow:0 2px 0 rgba(0,0,0,.2)}
.btn.grey{background:var(--btn-grey)}
.btn.coral{background:var(--coral)}
.ba-frame{left:662px;top:197px;width:389px;height:249px;background:#f4f4f4;border:5px solid #e6e6e6}
.ba-photo{left:5px;top:5px;width:369px;height:191px;background:linear-gradient(180deg,#c99a6f 0%,#e6c2a0 60%,#d8b08b 100%)}
.ba-labels{left:5px;top:174px;width:369px;height:22px;display:flex}
.ba-labels span{flex:1;font-size:11px;font-weight:600;color:#222;background:rgba(255,255,255,.55);padding:4px 7px;border-right:2px solid #f4f4f4}
.ba-caption{left:14px;top:205px;width:350px;font-size:9.5px;line-height:13px;color:#999}

/* treatment cards */
.card{top:513px;width:281px;height:199px;background:var(--white);box-shadow:0 1px 4px rgba(0,0,0,.12)}
.card-img{position:absolute;left:12px;top:12px;width:257px;height:145px}
.card-label{position:absolute;left:16px;top:168px;font-size:14px;color:var(--text)}
.card-bar{position:absolute;left:0;bottom:0;width:100%;height:5px}

/* welcome */
.portrait{left:232px;top:793px;width:228px;height:228px;border-radius:50%;background:radial-gradient(circle at 50% 55%,#d9a88a 0%,#a56a4c 55%,#f1f1f1 56%)}
.welcome-kicker{left:511px;top:808px;font-size:12px;color:#555}
.welcome-title{left:511px;top:830px;font-family:"Lato",sans-serif;font-weight:400;font-size:26px;color:var(--text)}
.welcome-copy{left:511px;top:876px;width:460px;font-size:12.5px;line-height:17.5px;color:var(--muted)}
.welcome-copy p+p{margin-top:17px}

/* consult band */
.consult{left:0;top:1101px;width:1200px;height:210px;background:var(--dark)}
.consult-title{left:0;top:1142px;width:1200px;text-align:center;font-family:"Lato",sans-serif;font-weight:300;font-size:28px;color:var(--white)}
.consult-sub{left:0;top:1183px;width:1200px;text-align:center;font-size:15px;color:var(--white)}

/* offers + prices */
.grey-area{left:0;top:1311px;width:1200px;height:470px;background:var(--light)}
.panel{top:1385px;height:270px;background:var(--white);border:1px solid #e4e4e4}
.panel-kicker{position:absolute;left:0;top:20px;width:100%;text-align:center;font-family:"Lato",sans-serif;font-size:16px;color:var(--text)}
.panel-rule{position:absolute;top:89px;height:1px;background:#ccc}
.offer-head{position:absolute;left:0;top:42px;width:100%;text-align:center;font-family:"Lato",sans-serif;font-weight:700;font-size:27px;color:var(--coral)}
.offer-head span{color:#a3a3a5}
.offer-copy{position:absolute;left:30px;top:106px;width:294px;text-align:center;font-size:12px;line-height:18px;color:#777}
.price-head{position:absolute;left:0;top:43px;width:100%;text-align:center;font-family:"Lato",sans-serif;font-size:28px;color:var(--text)}
.price-col{position:absolute;top:116px;width:222px}
.price-row{display:flex;justify-content:space-between;height:26.6px;align-items:center;padding:0 10px;font-size:11.5px;color:#999}
.price-row:nth-child(odd){background:#f1f1f1}

/* contact + map */
.map{left:0;top:1777px;width:1200px;height:319px;background:linear-gradient(135deg,#dcdcdc 0%,#e8e8e8 50%,#d6d6d6 100%)}
.contact-dark{left:155px;top:1735px;width:281px;height:80px;background:var(--dark);padding:22px 0 0 32px;color:var(--white)}
.contact-dark b{display:block;font-family:"Lato",sans-serif;font-weight:700;font-size:17px}
.contact-dark span{font-size:12px}
.contact-coral{left:436px;top:1735px;width:607px;height:80px;background:var(--coral)}
.pill{position:absolute;top:26px;height:28px;border-radius:14px;background:var(--white);display:flex;align-items:center;font-size:14px;color:#555}
.pill-icon{width:44px;height:28px;border-radius:14px 0 0 14px;background:var(--dark);display:flex;align-items:center;justify-content:center;margin-right:12px}
.address{left:460px;top:1901px;width:279px;height:75px;background:var(--white);text-align:center;padding-top:22px;font-size:13px;line-height:19px;color:#222}
.address:after{content:"";position:absolute;left:130px;bottom:-10px;border-left:10px solid transparent;border-right:10px solid transparent;border-top:10px solid var(--white)}
.pin{left:589px;top:1983px}

/* footer */
.footer{left:0;top:2096px;width:1200px;height:121px;background:var(--dark)}
.copyright{left:158px;top:2152px;font-size:11px;color:#c8c8c8}
.foot-social{left:579px;top:2147px;display:flex;gap:6px}
.foot-social .soc{background:#bdbdbf}
.foot-links{left:797px;top:2152px;font-size:11.5px;color:#c8c8c8;display:flex;gap:8px}
.foot-links .current{color:var(--coral)}
.to-top{left:1097px;top:2077px;width:38px;height:38px;border-radius:50%;background:var(--teal);display:flex;align-items:center;justify-content:center}
</style>
</head>
<body>
<div class="abs topline"></div>

<header>
  <div class="abs brand">
    <div class="brand-dot"></div>
    <div class="brand-name">NESSA PELBOURNE<br>AESTHETICS</div>
  </div>
  <div class="abs call">
    <svg width="20" height="18" viewBox="0 0 20 18"><path d="M2 6c0-3 4-4 8-4s8 1 8 4v1h-4V5H6v2H2z M5 8h10l2 8H3z" fill="#8c8c8e"/><circle cx="10" cy="12" r="2" fill="#fff"/></svg>
    Call Us: 0800 316 2270
  </div>
  <div class="abs social-top">
    <a class="soc on" aria-label="Social page one"></a>
    <a class="soc" aria-label="Social page two"></a>
  </div>
  <nav class="abs nav">
    <span class="active" style="left:0">Home</span>
    <span style="left:74px">Treatments</span>
    <span style="left:184px">Cosmetic Surgery</span>
    <span style="left:338px">Price List</span>
    <span style="left:437px">Gallery</span>
    <span style="left:518px">Contact</span>
    <svg style="position:absolute;left:605px;top:2px" width="16" height="16" viewBox="0 0 16 16"><circle cx="6.5" cy="6.5" r="5" fill="none" stroke="#333" stroke-width="2"/><path d="M10 10l5 5" stroke="#333" stroke-width="2"/></svg>
  </nav>
  <div class="abs nav-caret"></div>
</header>

<section>
  <div class="abs hero" role="img" aria-label="Surgical team working in an operating theatre"></div>
  <h1 class="abs hero-title">DERMIVA (R) Injections in<br>Plastic Surgery</h1>
  <p class="abs hero-copy">Lorem Ipsum is simply dummy text of the printing and typesetting industry loremhas been ...</p>
  <a class="abs btn grey" style="left:155px;top:384px;width:110px;height:31px">More Detail</a>
  <a class="abs btn grey" style="left:272px;top:384px;width:136px;height:31px">Photo Gallery</a>
  <svg class="abs" style="left:64px;top:309px" width="26" height="26" viewBox="0 0 26 26"><circle cx="13" cy="13" r="11.5" fill="none" stroke="#fff" stroke-width="2"/><path d="M15 8l-5 5 5 5" fill="none" stroke="#fff" stroke-width="2"/></svg>
  <svg class="abs" style="left:1110px;top:309px" width="26" height="26" viewBox="0 0 26 26"><circle cx="13" cy="13" r="11.5" fill="rgba(255,255,255,.2)" stroke="#9aa" stroke-width="2"/><path d="M11 8l5 5-5 5" fill="none" stroke="#dde" stroke-width="2"/></svg>
  <div class="abs ba-frame">
    <div class="abs ba-photo" role="img" aria-label="Before and after photos of a woman's frown lines over 120 days"></div>
    <div class="abs ba-labels"><span>Before</span><span>Day 7</span><span>Day 90</span><span>Day 120</span></div>
    <p class="abs ba-caption">Unretouched photos of paid models taken at maximum frown treatment with DERMIVA (R) Cosmetic.</p>
  </div>
</section>

<section>
  <a class="abs card" style="left:155px">
    <div class="card-img" role="img" aria-label="Mature woman's portrait showing wrinkle areas" style="background:linear-gradient(135deg,#f4e2c4,#d8a98a)"></div>
    <span class="card-label">Wrinkle Relaxing Injections &rarr;</span>
    <span class="card-bar" style="background:var(--amber)"></span>
  </a>
  <a class="abs card" style="left:460px">
    <div class="card-img" role="img" aria-label="Woman receiving a dermal filler injection" style="background:linear-gradient(135deg,#f3f3f3,#e2c8bc)"></div>
    <span class="card-label">Dermal Fillers &rarr;</span>
    <span class="card-bar" style="background:var(--red)"></span>
  </a>
  <a class="abs card" style="left:763px">
    <div class="card-img" role="img" aria-label="Woman receiving a chemical peel treatment" style="background:linear-gradient(135deg,#f1f1f1,#ecd2c0)"></div>
    <span class="card-label">Chemical Peel &rarr;</span>
    <span class="card-bar" style="background:var(--slate)"></span>
  </a>
</section>

<section>
  <div class="abs portrait" role="img" aria-label="Smiling woman with flowing hair"></div>
  <p class="abs welcome-kicker">Welcome to</p>
  <h2 class="abs welcome-title">Nessa Pelbourne Aesthetics</h2>
  <div class="abs welcome-copy">
    <p>Nessa is a registered nurse and independent nurse pr escriber with over 7 years experience in cosmetic medicine and facial injections.</p>
    <p>She is a member of the BCAP, NRC and insured with Ashby and Crane. She has worked with top plastic surgeons and dermatologists in NZ, Australia and the UK including Quenby Row.</p>
  </div>
</section>

<section>
  <div class="abs consult"></div>
  <h2 class="abs consult-title">Cosmetic Surgery Consultations with Mr. Tobias Renwick</h2>
  <p class="abs consult-sub">Consultations Priced: £130.00 (finance is available).</p>
  <a class="abs btn coral" style="left:429px;top:1233px;width:167px;height:32px">Contact Us Today</a>
  <a class="abs btn grey" style="left:603px;top:1233px;width:169px;height:32px">Cosmetic Surgery</a>
</section>

<section>
  <div class="abs grey-area"></div>
  <div class="abs panel" style="left:155px;width:355px">
    <p class="panel-kicker">Special Offers</p>
    <p class="offer-head">10% OFF <span>ON FRIDAY</span></p>
    <div class="panel-rule" style="left:26px;width:303px"></div>
    <p class="offer-copy">Call NPA today to take advantage<br>of our offers, Book in with the fabulous nurse<br>Imogen Now !</p>
    <a class="btn grey" style="position:absolute;left:93px;top:212px;width:170px;height:31px">Book Now! Today</a>
  </div>
  <div class="abs panel" style="left:536px;width:507px">
    <p class="panel-kicker">Price List</p>
    <p class="price-head">Nessa Pelbourne Aesthetics</p>
    <div class="panel-rule" style="left:25px;width:457px"></div>
    <div class="price-col" style="left:25px">
      <div class="price-row"><span>Dermiva® 1 Area</span><span>£100</span></div>
      <div class="price-row"><span>Dermiva® 2 Areas</span><span>£150</span></div>
      <div class="price-row"><span>Dermiva® 3 Areas</span><span>£200</span></div>
      <div class="price-row"><span>Dermiva for sweating</span><span>£350</span></div>
      <div class="price-row"><span>Dermal Fillers (0.5ml)</span><span>£100</span></div>
    </div>
    <div class="price-col" style="left:259px">
      <div class="price-row"><span>Dermal Fillers (1ml)</span><span>£200</span></div>
      <div class="price-row"><span>Lip Enhancement (0.5ml)</span><span>£100</span></div>
      <div class="price-row"><span>Lip Enhancement (1ml)</span><span>£200</span></div>
      <div class="price-row"><span>Chemical Peel</span><span>£65</span></div>
    </div>
  </div>
</section>

<section>
  <div class="abs map" role="img" aria-label="Street map around the clinic location"></div>
  <div class="abs contact-dark"><b>Contact</b><span>Nessa Pelbourne Aesthetics</span></div>
  <div class="abs contact-coral">
    <div class="pill" style="left:25px;width:203px">
      <span class="pill-icon"><svg width="14" height="12" viewBox="0 0 20 18"><path d="M2 6c0-3 4-4 8-4s8 1 8 4v1h-4V5H6v2H2z M5 8h10l2 8H3z" fill="var(--coral)"/></svg></span>020 7384 9102
    </div>
    <div class="pill" style="left:253px;width:331px">
      <span class="pill-icon"><svg width="14" height="10" viewBox="0 0 14 10"><rect width="14" height="10" fill="var(--coral)"/><path d="M0 0l7 5 7-5" fill="none" stroke="#4a4a4c" stroke-width="1.2"/></svg></span>npafenbrookbookings@mailbox.com
    </div>
  </div>
  <div class="abs address">18 Marlow Crescent, Hadleigh,<br>TN9 5RT</div>
  <svg class="abs pin" width="22" height="36" viewBox="0 0 22 36"><path d="M11 0C5 0 0 5 0 11c0 8 11 25 11 25s11-17 11-25C22 5 17 0 11 0z" fill="#333"/><circle cx="11" cy="11" r="4" fill="#fff"/></svg>
</section>

<footer>
  <div class="abs footer"></div>
  <p class="abs copyright">Copyright © 2015 - Nessa Pelbourne Aesthetics</p>
  <div class="abs foot-social"><a class="soc" aria-label="Social page one"></a><a class="soc" aria-label="Social page two"></a></div>
  <p class="abs foot-links"><span class="current">About Us</span>/<span>Contact Us</span>/<span>T&amp;C's</span>/<span>FAQ</span></p>
  <a class="abs to-top" aria-label="Back to top"><svg width="18" height="18" viewBox="0 0 18 18"><path d="M3 9l6-6 6 6M3 15l6-6 6 6" fill="none" stroke="#fff" stroke-width="2.4"/></svg></a>
</footer>
</body>
</html>
```